DOUBLE SIDED BROCHURE NEEDED TO PROMOTE DOCTOR

I need a double sided DL size (99mm x 210mm) brochure, promoting a doctor seeing patients in a new area.

I want something professional. I have included the relevant information. I would also like the Dr's picture somwhere in the brochure, with a professional background. I wish to print these tomorrow, so i will pick a winner within 14 hours of posting this ad.

I have included an example of a brochures design that I recently saw, and its definietly a good starting point.

Industry/Entity Type

Medical

```html
<!DOCTYPE html>
<html lang="en">
<head>
<meta charset="utf-8">
<title>Dr. Karim Haddad – Referral Brochure</title>
<link rel="stylesheet" href="https://fonts.googleapis.com/css2?family=Exo+2:wght@500;600;700&family=Open+Sans:wght@400;600;700&display=swap">
<style>
  :root{
    --page:#d9dcde;
    --teal-deep:#1b8d96;
    --teal:#3fb0b7;
    --teal-soft:#8fd3d6;
    --teal-pale:#c9ecec;
    --grey-light:#eceeef;
    --grey-mid:#d7dbdd;
    --ink:#2b2f31;
    --charcoal:#474d50;
    --white:#ffffff;
  }
  *{box-sizing:border-box;margin:0;padding:0}
  html,body{width:1200px;height:1192px;overflow:hidden}
  body{background:var(--page);font-family:"Open Sans",Arial,sans-serif;color:var(--ink);position:relative}
  .sprites{position:absolute;width:0;height:0}

  .panel{position:absolute;top:46px;width:520px;height:1100px;overflow:hidden;background:var(--grey-light);box-shadow:0 6px 18px rgba(0,0,0,.18)}
  .panel--front{left:53px}
  .panel--back{left:627px}
  .panel__art{position:absolute;inset:0;width:520px;height:1100px}
  .layer{position:absolute}

  .heading{font-family:"Exo 2",Arial,sans-serif;font-weight:700;color:var(--white);line-height:1.15}
  .icon{width:18px;height:18px;fill:currentColor;vertical-align:-3px;margin-right:6px}

  /* front */
  .intro{left:26px;right:26px;top:28px;color:var(--white)}
  .intro .heading{font-size:31px;margin-bottom:22px}
  .intro p{font-size:17px;line-height:1.4;margin-bottom:22px}
  .intro strong{font-weight:700}
  .hero-photo{left:0;top:340px;width:520px;height:470px;background:linear-gradient(180deg,#5f9fd8 0%,#a9cbe9 45%,#8a9096 75%,#5d6a70 100%)}
  .contact-tab{left:0;top:795px;background:var(--teal-deep);color:var(--white);font-family:"Exo 2",Arial,sans-serif;font-weight:700;font-size:21px;padding:9px 18px 9px 22px;border-radius:0 10px 10px 0;border:2px solid var(--teal-soft);border-left:none}
  .contact-list{left:24px;top:860px;font-size:18px;line-height:25px;color:var(--ink)}
  .contact-list .label{color:var(--teal-deep);font-weight:700}
  .contact-list .indent{padding-left:24px}
  .badge{left:318px;top:820px;width:190px;height:190px}
  .badge__text{left:318px;top:820px;width:190px;height:190px;display:flex;flex-direction:column;align-items:center;justify-content:center;text-align:center;font-family:"Exo 2",Arial,sans-serif;color:var(--ink)}
  .badge__top{color:var(--white);font-weight:700;font-size:24px;letter-spacing:.5px}
  .badge__mid{font-size:15px;font-weight:600;line-height:1.1}
  .badge__bottom{font-weight:700;font-size:22px}

  /* back */
  .profile-heading{left:24px;right:24px;top:30px;font-size:28px}
  .scope{left:24px;right:30px;top:182px;font-size:18px;line-height:1.4;color:var(--ink)}
  .services{left:24px;right:24px;list-style:none;font-size:18px;line-height:27px;color:var(--ink)}
  .services li{position:relative;padding-left:24px;margin-bottom:8px}
  .services li::before{content:"";position:absolute;left:2px;top:10px;width:9px;height:9px;border-radius:50%;background:var(--teal)}
  .services li.plain::before{display:none}
  .services--specialist{top:368px}
  .services--general{top:646px}
  .services--general li{margin-bottom:6px}
  .general-title{left:24px;top:598px;font-family:"Exo 2",Arial,sans-serif;font-weight:700;font-size:22px;color:var(--teal)}
  .portrait{left:300px;top:770px;width:220px;height:330px;background:linear-gradient(180deg,#bfc6ca 0%,#59636a 55%,#2d3438 100%)}
  .clinic{left:24px;top:915px;font-size:18px;line-height:24px;color:var(--white)}
  .clinic .gap{margin-top:18px}
  .clinic .small{font-size:12.5px;margin-top:14px}
  .clinic .fax{font-size:19px}
</style>
</head>
<body>

<svg class="sprites" aria-hidden="true">
  <defs>
    <symbol id="i-pin" viewBox="0 0 24 24"><path d="M12 2a7 7 0 0 0-7 7c0 5.2 7 13 7 13s7-7.8 7-13a7 7 0 0 0-7-7zm0 9.5A2.5 2.5 0 1 1 12 6.5a2.5 2.5 0 0 1 0 5z"/></symbol>
    <symbol id="i-phone" viewBox="0 0 24 24"><path d="M6.6 10.8a15.1 15.1 0 0 0 6.6 6.6l2.2-2.2a1 1 0 0 1 1-.25 11.4 11.4 0 0 0 3.6.57 1 1 0 0 1 1 1V20a1 1 0 0 1-1 1A17 17 0 0 1 3 4a1 1 0 0 1 1-1h3.5a1 1 0 0 1 1 1c0 1.25.2 2.45.57 3.57a1 1 0 0 1-.25 1z"/></symbol>
    <symbol id="i-fax" viewBox="0 0 24 24"><path d="M7 3h8l3 3v4H7zM4 10h16a2 2 0 0 1 2 2v7a2 2 0 0 1-2 2H4a2 2 0 0 1-2-2v-7a2 2 0 0 1 2-2zm3 4v2h2v-2zm4 0v2h2v-2zm4 0v2h2v-2z"/></symbol>
    <linearGradient id="g-teal" x1="0" y1="0" x2="0" y2="1">
      <stop offset="0" stop-color="#1f95a0"/>
      <stop offset="1" stop-color="#62c3c8"/>
    </linearGradient>
    <linearGradient id="g-grey" x1="0" y1="0" x2="0" y2="1">
      <stop offset="0" stop-color="#f7f8f8"/>
      <stop offset="1" stop-color="#d5d9db"/>
    </linearGradient>
  </defs>
</svg>

<!-- FRONT -->
<section class="panel panel--front" aria-label="Brochure front">
  <div class="layer hero-photo" role="img" aria-label="Photograph of the surgeon in front of a modern hospital building under a blue sky"></div>

  <svg class="panel__art" viewBox="0 0 520 1100" aria-hidden="true">
    <path d="M0 0H520V330C400 300 260 395 0 360Z" fill="url(#g-teal)"/>
    <path d="M0 360C260 395 400 300 520 330V352C400 326 260 420 0 382Z" fill="var(--teal-pale)" opacity=".9"/>
    <path d="M0 770C170 730 330 800 520 760V790C330 830 170 765 0 800Z" fill="var(--teal)"/>
    <path d="M0 800C170 765 330 830 520 790V1100H0Z" fill="url(#g-grey)"/>
    <rect x="0" y="1068" width="520" height="32" fill="var(--charcoal)"/>
  </svg>

  <div class="layer intro">
    <h1 class="heading">Dear Doctors,</h1>
    <p>We are pleased to announce that <strong>Dr. Karim Haddad</strong> is now consulting in Coastal Bay, seeing public and private patients.</p>
    <p>Guaranteed appointment within two weeks, with patients having the option of surgery at Harbour Health Campus, Westfield General Hospital or St. Clare Private Hospital.</p>
  </div>

  <div class="layer contact-tab">CONTACT DETAILS:</div>

  <div class="layer contact-list">
    <div class="label"><svg class="icon"><use href="#i-pin"/></svg>Coastal Bay Clinic:</div>
    <div class="indent">42 Seabreeze Road</div>
    <div class="indent">Coastal Bay WA 6199</div>
    <div class="label"><svg class="icon"><use href="#i-phone"/></svg>Phone:</div>
    <div class="indent">1300 000 482</div>
    <div class="label"><svg class="icon"><use href="#i-fax"/></svg>Please send all referrals by fax to</div>
    <div class="indent">(08) 6000 2841</div>
  </div>

  <svg class="layer badge" viewBox="0 0 190 190" aria-hidden="true">
    <g fill="var(--teal)" transform="translate(95 95)">
      <rect x="-70" y="-70" width="140" height="140"/>
      <rect x="-70" y="-70" width="140" height="140" transform="rotate(22.5)"/>
      <rect x="-70" y="-70" width="140" height="140" transform="rotate(45)"/>
      <rect x="-70" y="-70" width="140" height="140" transform="rotate(67.5)"/>
    </g>
    <circle cx="95" cy="95" r="72" fill="none" stroke="var(--teal-pale)" stroke-width="2"/>
  </svg>
  <div class="layer badge__text">
    <span class="badge__top">GUARANTEED</span>
    <span class="badge__mid">appointment within</span>
    <span class="badge__bottom">TWO WEEKS</span>
  </div>
</section>

<!-- BACK -->
<section class="panel panel--back" aria-label="Brochure back">
  <svg class="panel__art" viewBox="0 0 520 1100" aria-hidden="true">
    <rect width="520" height="1100" fill="var(--white)"/>
    <path d="M0 0H520V140C380 175 200 130 0 160Z" fill="url(#g-teal)"/>
    <path d="M0 285C170 250 340 310 520 270V300C340 340 170 280 0 315Z" fill="var(--teal)"/>
    <path d="M0 315C170 280 340 340 520 300V1100H0Z" fill="url(#g-grey)"/>
    <path d="M0 830C170 800 340 870 520 820V1100H0Z" fill="var(--teal-pale)"/>
    <path d="M0 846C170 818 340 888 520 840V1100H0Z" fill="var(--teal)"/>
  </svg>

  <h2 class="layer heading profile-heading">Dr. Karim Haddad is a highly trained specialised surgeon.</h2>
  <p class="layer scope">in all areas of Endocrine, Breast and General Surgery. Including;</p>

  <ul class="layer services services--specialist">
    <li>Thyroid Surgery</li>
    <li>Parathyroid surgery<br>(including minimally invasive parathyroidectomy)</li>
    <li>Breast Cancer<br>Benign breast lesions</li>
  </ul>

  <h3 class="layer general-title">All areas of general surgery, such as:</h3>
  <ul class="layer services services--general">
    <li>Gallbladder surgery</li>
    <li>Hernia surgery</li>
    <li>Haemorrhoids</li>
    <li>Carpal Tunnel</li>
    <li>Vasectomy etc etc…</li>
  </ul>

  <div class="layer portrait" role="img" aria-label="Portrait photograph of the surgeon in a dark suit"></div>

  <div class="layer clinic">
    <div>Coastal Bay Clinic:</div>
    <div><svg class="icon"><use href="#i-pin"/></svg>42 Seabreeze Road</div>
    <div>Coastal Bay WA 6199</div>
    <div class="gap"><svg class="icon"><use href="#i-phone"/></svg>1300 000 482</div>
    <div class="small"><svg class="icon"><use href="#i-fax"/></svg>Please send all referrals by fax to</div>
    <div class="fax">(08) 6000 2841</div>
  </div>
</section>

</body>
</html>
```